Web Design - 1 page for Buy - Repair - Service - Upgrade - PC Maintenance

We specialize in consumer and small business. It will be mobile friendly, viewable on all devices. Fully editable at the text level of the sections !!! - HTML / CSS only to be able to add a section would be to the web site
Updates

Target Market(s)

consumer and small business IT.

Coding

Coded - Design and coding required

Number of Pages Required

1 page

Font styles to use
Sans Serif

Requirements
Must have
• Looking for a page with a design that compliments the business card and pamphlet that has already been made (attached files). It should look professional and easy to read business. Email and phone number should be visible when the page loads. I do not want any forms for people to mess with. No "Contact Us" form or enter in email for newsletter. Customers will just be looking for this site to confirm we are professionals and have our business in order. OpenStreetMap: embedding map in webpage (like Google Maps) to where the workshop is located
Nice to have
• 2vask.com => this style of website would be more modern visually by integrating higher demands

```html
<!DOCTYPE html>
<html lang="en">
<head>
<meta charset="utf-8">
<title>Vertex Bay IT — Buy, Repair, Service, Upgrade</title>
<link href="https://fonts.googleapis.com/css2?family=Montserrat:wght@300;400;600;700&family=Open+Sans:wght@400&display=swap" rel="stylesheet">
<style>
  :root{
    --blue:#2a8fd6;
    --blue-deep:#16497f;
    --blue-mid:#2468a8;
    --ink:#222528;
    --text:#7a7d80;
    --grey-band:#f3f3f3;
    --white:#ffffff;
    --footer:#151617;
    --square:rgba(42,143,214,0.06);
  }
  *{box-sizing:border-box;margin:0;padding:0}
  html,body{width:1200px;height:4489px;overflow:hidden}
  body{background:var(--white);font-family:"Open Sans",Arial,sans-serif;color:var(--text)}

  .hero{position:relative;height:500px;background:linear-gradient(160deg,var(--blue-mid) 0%,var(--blue-deep) 55%,#0f3563 100%);color:var(--white);text-align:center}
  .hero-brand{position:absolute;top:140px;left:0;right:0;display:flex;justify-content:center;align-items:center;gap:18px;font-family:"Montserrat",sans-serif;font-weight:700;font-size:52px;letter-spacing:2px}
  .brand-mark{width:26px;height:26px;background:var(--white)}
  .hero-rule{position:absolute;top:291px;left:440px;width:320px;height:1px;background:rgba(255,255,255,0.6)}
  .hero-contact{position:absolute;left:0;right:0;display:flex;justify-content:center;align-items:center;gap:20px;font-family:"Montserrat",sans-serif;font-weight:300;font-size:31px}
  .hero-contact.phone{top:336px}
  .hero-contact.email{top:406px}
  .scroll-cue{position:absolute;left:570px;top:470px;width:60px;height:60px;border-radius:50%;background:var(--white);box-shadow:0 0 0 6px rgba(0,0,0,0.04);display:flex;align-items:center;justify-content:center;z-index:2}

  .intro{height:391px;padding-top:105px;text-align:center}
  .intro-title{font-family:"Montserrat",sans-serif;font-weight:600;font-size:40px;line-height:44px;color:var(--blue);letter-spacing:2px}
  .intro-rule{width:80px;height:1px;background:#cfd3d6;margin:26px auto 34px}
  .intro-text{width:1020px;margin:0 auto;font-size:15px;line-height:26px}

  .service{position:relative;height:348px;overflow:hidden}
  .service.band{background:var(--grey-band)}
  .service .sq{position:absolute;background:var(--square)}
  .service-visual{position:absolute;top:29px;width:420px;height:290px;border-radius:4px}
  .service.media-left .service-visual{left:165px}
  .service.media-right .service-visual{left:660px}
  .service-copy{position:absolute;top:108px;width:510px}
  .service.media-left .service-copy{left:615px}
  .service.media-right .service-copy{left:84px}
  .service-title{display:flex;align-items:center;gap:22px;font-family:"Montserrat",sans-serif;font-weight:700;font-size:24px;color:var(--ink);letter-spacing:1px;margin-bottom:18px}
  .service-title::before{content:"";width:60px;height:2px;background:var(--blue);flex:none}
  .service-text{font-size:14px;line-height:24px}

  .footer{position:relative;height:466px;background:var(--footer);color:#bfc3c6}
  .footer-map{position:absolute;left:150px;top:57px;width:525px;height:340px;background:linear-gradient(135deg,#f2efe6,#e6e3da)}
  .footer-map svg{position:absolute;left:250px;top:150px}
  .footer-info{position:absolute;left:790px;top:68px;font-family:"Montserrat",sans-serif}
  .footer-heading{color:var(--white);font-weight:600;font-size:16px;letter-spacing:1px;margin-bottom:22px}
  .footer-line{display:flex;align-items:center;gap:14px;font-size:14px;margin-bottom:16px}
  .footer-social{display:flex;gap:12px;margin:26px 0 30px}
  .footer-social span{width:32px;height:32px;border-radius:50%;background:var(--white)}
  .footer-brand{display:flex;align-items:center;gap:10px;color:var(--white);font-weight:700;font-size:22px;letter-spacing:1px}
  .footer-brand .brand-mark{width:12px;height:12px;background:var(--blue)}
  .footer-copy{margin-top:42px;font-size:13px}
</style>
</head>
<body>

<header class="hero" role="img" aria-label="Blue toned close-up of a circuit board behind the header">
  <div class="hero-brand"><span class="brand-mark"></span>VERTEX BAY IT</div>
  <div class="hero-rule"></div>
  <div class="hero-contact phone">
    <svg width="22" height="36" viewBox="0 0 22 36" fill="none" stroke="#fff" stroke-width="2"><rect x="1" y="1" width="20" height="34" rx="3"/><line x1="8" y1="30" x2="14" y2="30"/></svg>
    <span>123 - 456 - 7890</span>
  </div>
  <div class="hero-contact email">
    <svg width="40" height="28" viewBox="0 0 40 28" fill="none" stroke="#fff" stroke-width="2"><rect x="1" y="1" width="38" height="26"/><polyline points="1,1 20,16 39,1"/></svg>
    <span>info@vertexbayit.com</span>
  </div>
  <div class="scroll-cue">
    <svg width="16" height="26" viewBox="0 0 16 26" fill="none" stroke="#8a8f93" stroke-width="1.6"><rect x="1" y="1" width="14" height="24" rx="7"/><line x1="8" y1="6" x2="8" y2="10"/></svg>
  </div>
</header>

<section class="intro">
  <h1 class="intro-title">BUY - REPAIR - SERVICE -<br>- UPGRADE - MAINTENACE PC &amp; LAPTOP</h1>
  <div class="intro-rule"></div>
  <p class="intro-text">Lorem Ipsum is simply dummy text of the printing and typesetting industry. Lorem Ipsum has been the industry's standard dummy text ever since the 1500s, when an unknown printer took a galley of type and scrambled it to make a type specimen book. It has survived not only five centuries, but also the leap into electronic typesetting, remaining essentially unchanged.</p>
</section>

<section class="service band media-left">
  <span class="sq" style="left:1040px;top:40px;width:60px;height:60px"></span>
  <span class="sq" style="left:1110px;top:110px;width:40px;height:40px"></span>
  <div class="service-visual" role="img" aria-label="Smiling technician holding an open laptop" style="background:linear-gradient(180deg,#e6eef5,#b9cfe6)"></div>
  <div class="service-copy">
    <h2 class="service-title">HONEST SERVICE</h2>
    <p class="service-text">Our certified technicians aren't paid on commission. No pressure to upgrade to products/services you don't need or want. Even the best computers will eventually break down, and if we leave you happy, that's when we hope you'll come back to us.</p>
  </div>
</section>

<section class="service media-right">
  <span class="sq" style="left:30px;top:60px;width:50px;height:50px"></span>
  <span class="sq" style="left:90px;top:250px;width:70px;height:70px"></span>
  <div class="service-visual" role="img" aria-label="Figure with a shield defending a laptop from a red virus" style="background:linear-gradient(135deg,#eeeeee,#d9d9d9 60%,#c0392b)"></div>
  <div class="service-copy">
    <h2 class="service-title">MALWARE/VIRUS REMOVAL</h2>
    <p class="service-text">Infections can come from many places and sometimes antivirus just isn't enough. We can get your system back to top shape, and train users how to avoid pitfalls in the future, which is better than any antivirus you could buy!</p>
  </div>
</section>

<section class="service band media-left">
  <span class="sq" style="left:1050px;top:50px;width:60px;height:60px"></span>
  <div class="service-visual" role="img" aria-label="Technician repairing an open desktop computer with tools" style="background:linear-gradient(180deg,#e9e5df,#8d8b88)"></div>
  <div class="service-copy">
    <h2 class="service-title">PC/DESKTOP/LAPTOP HARDWARE<br>REPAIR</h2>
    <p class="service-text">Find out exactly which part of your computer is failing and causing trouble. Our professionals will find the best value replacement and install it, good as new.</p>
  </div>
</section>

<section class="service media-right">
  <span class="sq" style="left:40px;top:40px;width:60px;height:60px"></span>
  <span class="sq" style="left:100px;top:240px;width:50px;height:50px"></span>
  <div class="service-visual" role="img" aria-label="Desktop computer with colourful screen, keyboard and mouse" style="background:linear-gradient(180deg,#f2f2f2,#6e5aa8 55%,#2b2b2b)"></div>
  <div class="service-copy">
    <h2 class="service-title">UPGRADES</h2>
    <p class="service-text">A new video card to play the latest game at the highest settings? A new disk to give your laptop a very noticeable speed boost? Or maybe just the latest and greatest version of your operating system to keep you secure. We can make the upgrade hassle-free.</p>
  </div>
</section>

<section class="service band media-left">
  <span class="sq" style="left:1060px;top:60px;width:50px;height:50px"></span>
  <div class="service-visual" role="img" aria-label="Word cloud illustration about data migration" style="background:linear-gradient(180deg,#eef1ee,#c9d9c4 45%,#d47a7a)"></div>
  <div class="service-copy">
    <h2 class="service-title">DATA MIGRATION</h2>
    <p class="service-text">We can make your new computer feel like an old friend. Transfer all your files, photos, bookmarks, email accounts, personal settings, etc. to a new computer and put them right where you left them.</p>
  </div>
</section>

<section class="service media-right">
  <span class="sq" style="left:30px;top:50px;width:70px;height:70px"></span>
  <div class="service-visual" role="img" aria-label="Hard drive resting in a red and white life ring" style="background:linear-gradient(135deg,#f4f4f4,#c9ccd0 55%,#d64a3a)"></div>
  <div class="service-copy">
    <h2 class="service-title">DATA RESCUE</h2>
    <p class="service-text">Flash drive formatted? Hard Drive corrupted? Data loss can be devastating, but sometimes recovery is possible for precious photos and important documents. If our best tools can't get your files back, you won't be charged.</p>
  </div>
</section>

<section class="service band media-left">
  <span class="sq" style="left:1050px;top:40px;width:60px;height:60px"></span>
  <div class="service-visual" role="img" aria-label="Orange figure carrying stacked files out of a laptop screen" style="background:linear-gradient(180deg,#f1f1f1,#e8a24a 50%,#9aa3ab)"></div>
  <div class="service-copy">
    <h2 class="service-title">TUNE UPS</h2>
    <p class="service-text">Over time, systems can get slowed down by unnecessary files and programs demanding attention from your processor and memory that should instead be doing work for you! We can clean-up (and physically clean out) your system to get it running at peak performance.</p>
  </div>
</section>

<section class="service media-right">
  <span class="sq" style="left:40px;top:60px;width:50px;height:50px"></span>
  <div class="service-visual" role="img" aria-label="Technician setting up a desktop computer with a customer at home" style="background:linear-gradient(180deg,#eef2f5,#9fb5c8)"></div>
  <div class="service-copy">
    <h2 class="service-title">IN-HOME INSTALLATION</h2>
    <p class="service-text">All our services come with pick-up and drop-off installation. You won't be left to set up wireless networking, cables, controllers, and printers by yourself!</p>
  </div>
</section>

<section class="service band media-left">
  <span class="sq" style="left:1040px;top:60px;width:60px;height:60px"></span>
  <div class="service-visual" role="img" aria-label="Hand reaching out of a laptop screen to press a key" style="background:linear-gradient(180deg,#f0f0f0,#bfc3c7)"></div>
  <div class="service-copy">
    <h2 class="service-title">REMOTE SUPPORT</h2>
    <p class="service-text">Small problems shouldn't cost an arm and a leg to fix. We'll set up remote support to your computer to efficiently and cost effectively solve what can be solved without the need of a sending a technician over.</p>
  </div>
</section>

<footer class="footer">
  <div class="footer-map" role="img" aria-label="Street map showing the workshop location">
    <svg width="26" height="38" viewBox="0 0 26 38"><path d="M13 1C6 1 1 6 1 13c0 9 12 24 12 24s12-15 12-24C25 6 20 1 13 1z" fill="#2a8fd6"/><circle cx="13" cy="13" r="5" fill="#fff"/></svg>
  </div>
  <div class="footer-info">
    <div class="footer-heading">CONTACT INFO</div>
    <div class="footer-line">
      <svg width="14" height="14" viewBox="0 0 24 24" fill="#2a8fd6"><path d="M6.6 10.8a15 15 0 0 0 6.6 6.6l2.2-2.2a1 1 0 0 1 1-.25 11.4 11.4 0 0 0 3.6.57 1 1 0 0 1 1 1V20a1 1 0 0 1-1 1A17 17 0 0 1 3 4a1 1 0 0 1 1-1h3.5a1 1 0 0 1 1 1c0 1.25.2 2.45.57 3.57a1 1 0 0 1-.25 1z"/></svg>
      <span>123 - 456 - 7890</span>
    </div>
    <div class="footer-line">
      <svg width="16" height="12" viewBox="0 0 16 12" fill="none" stroke="#2a8fd6" stroke-width="1.5"><rect x="0.75" y="0.75" width="14.5" height="10.5"/><polyline points="0.75,0.75 8,6.5 15.25,0.75"/></svg>
      <span>info@vertexbayit.com</span>
    </div>
    <div class="footer-social"><span></span><span></span><span></span></div>
    <div class="footer-brand"><span class="brand-mark"></span>VERTEX BAY IT</div>
    <p class="footer-copy">Copyright © 2018 &nbsp;|&nbsp; All Rights Reserved.</p>
  </div>
</footer>

</body>
</html>
```